Cryptocurrency Advisor Business Card

Dravelin Consulting Services is my company, which advises many projects in the ICO/Cryptocurrency industry. I'd like to get a sleek, preferably matte black or matte dark blue finish, business card with the company name (and simple logo w/ crypto feel) on one side and while the other side I'd like a small twitter and telegram logo together maybe separated by a / as it's the same, then an email and a phone logo so I can insert those specifics there (no address). Can have name then CEO section too. At the bottom of that section, find a place for more of a job description: ICO Advisor, World Champion Gamer, Esports Award Winner, Quorvane Expert. You can possibly design a simple logo or use something with a crypto twist or background, but nothing too complex. Rounded edges for printing not square.
Updates

Had personal issues taking a few days away from me being able to provide feedback and check designs, etc. Will be more active now finalizing design just needed few days from issue but all is sorted.

Target Market(s)

Cryptocurrency industry

Industry/Entity Type

Management Consulting

Contact Information for Business Card

Font styles to use
Sans Serif

Colors
5c5c5c
474747
757575
9d9d9d
aaaaaa
333333
0355a3

Requirements
Must have
• Refer to Details/Description
Nice to have
Should not have
• Address section

```html
<!DOCTYPE html>
<html lang="en">
<head>
<meta charset="UTF-8">
<title>Dravelin Consulting Services – Business Card</title>
<link rel="stylesheet" href="https://fonts.googleapis.com/css2?family=Nunito:wght@800&family=Nunito+Sans:wght@400&display=swap">
<style>
  :root {
    --backdrop: #3a3a3a;
    --card: #2e2e2e;
    --card-edge: #262626;
    --mark-dark: #222222;
    --ink-light: #aaaaaa;
    --ink-mid: #9d9d9d;
    --ink-soft: #c4c4c4;
    --band-dark: #474747;
    --band-light: #aaaaaa;
    --rule: #5c5c5c;
  }
  * { box-sizing: border-box; margin: 0; padding: 0; }
  html, body {
    width: 1200px; height: 972px; overflow: hidden;
    background: var(--backdrop);
  }
  .sheet { position: relative; width: 1200px; height: 972px; }
  .card {
    position: absolute; left: 220px; width: 760px; height: 430px;
    background: var(--card);
    border-radius: 14px;
    overflow: hidden;
    box-shadow: 0 0 0 1px var(--card-edge);
  }
  .card--front { top: 40px; }
  .card--back { top: 502px; }

  .company-name {
    font-family: "Nunito", sans-serif; font-weight: 800;
    line-height: 1.12;
  }

  /* Front */
  .front-brand {
    position: absolute; inset: 0;
    display: flex; align-items: center; justify-content: center; gap: 28px;
  }
  .front-brand__square {
    width: 104px; height: 104px; background: var(--mark-dark);
  }
  .front-brand .company-name { font-size: 44px; color: var(--ink-mid); }

  /* Back */
  .back-brand {
    position: absolute; left: 40px; top: 118px;
    display: flex; align-items: center; gap: 20px;
  }
  .back-brand__square {
    width: 80px; height: 80px; background: var(--ink-light); flex: none;
  }
  .back-brand .company-name { font-size: 27px; color: var(--ink-light); }
  .divider {
    position: absolute; left: 442px; top: 70px; width: 1px; height: 210px;
    background: var(--rule);
  }
  .contact {
    position: absolute; left: 474px; top: 92px;
    font-family: "Nunito Sans", sans-serif; color: var(--ink-soft);
  }
  .contact__name {
    font-family: "Nunito", sans-serif; font-weight: 800;
    font-size: 32px; color: var(--ink-light); line-height: 1;
  }
  .contact__role { font-size: 17px; margin-top: 4px; margin-bottom: 22px; }
  .contact__list { list-style: none; }
  .contact__item {
    display: flex; align-items: center; gap: 12px;
    font-size: 19px; line-height: 27px;
  }
  .contact__icon { width: 20px; height: 20px; flex: none; }
  .contact__social-dot {
    width: 16px; height: 16px; border-radius: 50%;
    background: var(--ink-soft); margin: 0 2px;
  }
  .tagline {
    position: absolute; left: 40px; right: 40px; top: 322px;
    font-family: "Nunito Sans", sans-serif; font-size: 18px;
    color: var(--ink-soft); white-space: nowrap;
  }
  .band {
    position: absolute; left: 0; right: 0; bottom: 0; height: 18px;
    display: flex;
  }
  .band__dark { flex: 1; background: var(--band-dark); }
  .band__light { flex: 1; background: var(--band-light); }
</style>
</head>
<body>
<main class="sheet">
  <section class="card card--front" aria-label="Card front">
    <div class="front-brand">
      <div class="front-brand__square"></div>
      <div class="company-name">Dravelin<br>Consulting Services</div>
    </div>
  </section>

  <section class="card card--back" aria-label="Card back">
    <div class="back-brand">
      <div class="back-brand__square"></div>
      <div class="company-name">Dravelin<br>Consulting Services</div>
    </div>
    <div class="divider"></div>
    <div class="contact">
      <h1 class="contact__name">Teodor Vance</h1>
      <p class="contact__role">CEO</p>
      <ul class="contact__list">
        <li class="contact__item">
          <svg class="contact__icon" viewBox="0 0 24 24" fill="none" stroke="#c4c4c4" stroke-width="1.8" stroke-linecap="round" stroke-linejoin="round"><path d="M5 3h4l2 5-2.5 1.5a11 11 0 0 0 6 6L16 13l5 2v4a2 2 0 0 1-2 2A16 16 0 0 1 3 5a2 2 0 0 1 2-2z"/></svg>
          <span>+000 5550 12345</span>
        </li>
        <li class="contact__item">
          <svg class="contact__icon" viewBox="0 0 24 24" fill="none" stroke="#c4c4c4" stroke-width="1.8" stroke-linejoin="round"><rect x="2.5" y="5" width="19" height="14"/><path d="M2.5 5l9.5 8 9.5-8"/></svg>
          <span>teo@dravelin.com</span>
        </li>
        <li class="contact__item">
          <svg class="contact__icon" viewBox="0 0 24 24" fill="none" stroke="#c4c4c4" stroke-width="1.6"><circle cx="12" cy="12" r="9.5"/><ellipse cx="12" cy="12" rx="4.5" ry="9.5"/><path d="M2.5 12h19M4 7h16M4 17h16"/></svg>
          <span>www.dravelin.com</span>
        </li>
        <li class="contact__item">
          <span class="contact__social-dot"></span>
          <span>dravelinconsult</span>
        </li>
      </ul>
    </div>
    <p class="tagline">ICO Advisor • World Champion Gamer • Esports Award Winner • Quorvane Expert.</p>
    <div class="band"><span class="band__dark"></span><span class="band__light"></span></div>
  </section>
</main>
</body>
</html>
```